Business Card: RW Office Partners - Your organised problem solver

Business Name: RW Office Partners
Website: www.rwofficepartners-example.com.au
Email: maribel@rwofficepartners-example.com.au
Mobile: 61 400 000 000
Facebook: @rwofficepartners
Instrgram: @rwofficepartners

Brading Colours:
HEX
#986474
#ddccd3
#7a8498
#c9d8e4
#000000
#ffffff

Tag Line: Your organised problem solver

Link to DRAFT website:
https://draftsites-example.com/rw-office-partners

About Page from the website:
My name is Maribel Rowe, and I would love to assist you to become more productive in your day to day and achieve your business and personal goals.
My mission is to give you time, time to work on the important tasks of your business or to be able to spend more time with your family. I will take on the tasks you don’t have time for, don’t know well or simply don’t like to do.
I have an extensive background in Administration, Tender Coordination, Document Control, WHS and Quality Management working primarily in the Construction, Mining and Corporate World.
I am passionate about being organised, having order and making things in your life (and mine) easier! I love to watch something unfold and grow into something amazing! I am known for being the go-to problem solver, the organiser of all things, producing high standards of work even under pressure. I’m also a confident communicator, and I understand that you’re busy running your business.

Target Market(s)

Small to Medium Business who require assistance in their business by a virtual assistant.

Industry/Entity Type

Virtual Assistant

Contact Information for Business Card

Mobile: 61 400 000 000

Font styles to use
Sans Serif

Colors
ffffff

Requirements
Must have
• Branding Colours as outlined.
Contact Details as outlined.
Logo as provided.
Proper contact details - mobile, facebook, instragm, website.
Simple, Elegant, very clean looking.
Should not have
• Note cute with pictures.
Not too girly as still want to market to construction companies.

```html
<!DOCTYPE html>
<html lang="en">
<head>
<meta charset="utf-8">
<title>RW Office Partners – Business Card</title>
<link rel="stylesheet" href="https://fonts.googleapis.com/css2?family=Montserrat:wght@600&family=Roboto:wght@300;400&display=swap">
<style>
  :root {
    --brand-rose: #986474;
    --brand-slate: #7a8498;
    --card-black: #1f1f20;
    --stage: #38383a;
    --text-white: #ffffff;
    --text-soft: #e9e9ec;
  }
  * { box-sizing: border-box; margin: 0; padding: 0; }
  html, body { width: 1200px; height: 900px; overflow: hidden; }
  body {
    background: var(--stage);
    font-family: "Roboto", Arial, sans-serif;
    position: relative;
  }
  .card {
    position: absolute;
    left: 270px;
    width: 660px;
    height: 377px;
    background: var(--card-black);
    box-shadow: 0 10px 30px rgba(0,0,0,0.45);
  }
  .card--front { top: 50px; }
  .card--back { top: 473px; display: flex; align-items: center; justify-content: center; }

  .brand-name {
    position: absolute;
    left: 48px;
    top: 78px;
    font-family: "Montserrat", Arial, sans-serif;
    font-weight: 600;
    font-size: 31px;
    line-height: 1.08;
    letter-spacing: 0.5px;
    text-transform: uppercase;
    color: var(--brand-slate);
  }
  .divider {
    position: absolute;
    left: 300px;
    top: 112px;
    width: 2px;
    height: 122px;
    background: var(--brand-rose);
  }
  .contact-list {
    position: absolute;
    left: 318px;
    top: 118px;
    list-style: none;
  }
  .contact-list li {
    display: flex;
    align-items: center;
    gap: 7px;
    height: 28px;
    font-size: 15px;
    color: var(--text-white);
    white-space: nowrap;
  }
  .contact-list svg { width: 13px; height: 13px; flex: none; }
  .social-mark {
    width: 11px; height: 11px;
    background: var(--brand-slate);
    border-radius: 2px;
    flex: none;
  }
  .tagline {
    position: absolute;
    left: 48px;
    top: 262px;
    font-size: 16px;
    font-weight: 300;
    color: var(--text-soft);
  }
  .back-name {
    font-family: "Montserrat", Arial, sans-serif;
    font-weight: 600;
    font-size: 44px;
    letter-spacing: 1px;
    text-transform: uppercase;
    color: var(--brand-rose);
  }
</style>
</head>
<body>
  <section class="card card--front" aria-label="Business card front">
    <div class="brand-name">RW Office<br>Partners</div>
    <div class="divider"></div>
    <ul class="contact-list">
      <li>
        <svg viewBox="0 0 16 16" aria-hidden="true"><path fill="#986474" d="M3.5 1.5l2.5 0 1 3.5-1.6 1.2a8 8 0 0 0 4.4 4.4L11 9l3.5 1v2.5c0 1-1 2-2 2A11 11 0 0 1 1.5 3.5c0-1 1-2 2-2z"/></svg>
        61 400 000 000
      </li>
      <li>
        <svg viewBox="0 0 16 16" aria-hidden="true"><rect x="1" y="3" width="14" height="10" rx="1" fill="#986474"/><path d="M1.5 3.8L8 8.8l6.5-5" stroke="#1f1f20" stroke-width="1.4" fill="none"/></svg>
        maribel@rwofficepartners-example.com.au
      </li>
      <li>
        <svg viewBox="0 0 16 16" aria-hidden="true"><circle cx="8" cy="8" r="6.5" fill="none" stroke="#986474" stroke-width="1.6"/><path d="M1.5 8h13M8 1.5c-3 3.5-3 9.5 0 13M8 1.5c3 3.5 3 9.5 0 13" stroke="#986474" stroke-width="1.2" fill="none"/></svg>
        www.rwofficepartners-example.com.au
      </li>
      <li>
        <span class="social-mark"></span>
        @rwofficepartners
      </li>
    </ul>
    <p class="tagline">Your organised problem solver</p>
  </section>

  <section class="card card--back" aria-label="Business card back">
    <div class="back-name">RW Office Partners</div>
  </section>
</body>
</html>
```